依頼詳細
デザインテイストのイメージは以下の通りです
・洗練された
・安心感のある
・落ち着いた
・信頼できる

「写真素材について」
事業所画像など一部提供可能ですが、基本的にはミルテフォトなどの素材もしくはイラストとの組み合わせでお願いいたします

「WFと原稿について」
レイアウトについてはある程度自由に変更していただいても結構です

「納品形態について」
psd xd aiなど劣化のないものであればなんでも大丈夫です

「選考のポイント」
デザイン性のみ
SEOやマーケティング的な提案は求めていません
元サイトURL一応載せておきますが形式的に作成したものですので
こちらと比較してのアドバイスなども求めていません
あくまでデザインで決めます

サイトURL
http://kurete-kaigo.net/
ページ数
5ページ
希望イメージ
シンプル 複雑
単色 カラフル
暗い 明るい
日常 高級
遊び心 厳粛
未来的 伝統的
女性的 男性的
希望する色
青系、水色系
納品ファイル
• 高解像度JPG (.jpg)
• イラストレーター形式 (.ai)
• フォトショップ形式 (.psd)
• PNG形式 (.png)
補足説明
提案の数が少ないので期限を延長いたします
■ 選んだ理由

限定された条件のなかで素晴らしいデザインをご提案いただきありがとうございました

■ 提案者全員のお礼・コメント

素材画像がない状態でのデザイン制作は難しかったと思います
その中で素晴らしい提案をいただきまして本当にありがとうございました

```html
<!DOCTYPE html>
<html lang="ja">
<head>
<meta charset="utf-8">
<title>訪問介護そよぎ</title>
<link href="https://fonts.googleapis.com/css2?family=Noto+Sans+JP:wght@300;400;500;700&display=swap" rel="stylesheet">
<style>
:root{
  --ink:#333a40;
  --muted:#6b7580;
  --blue:#5aa6d6;
  --blue-soft:#a8d2ee;
  --blue-pale:#e4f2fb;
  --blue-mid:#8ec3e6;
  --white:#ffffff;
}
*{margin:0;padding:0;box-sizing:border-box}
html,body{width:1200px;height:5236px;overflow:hidden}
body{position:relative;background:var(--white);color:var(--ink);font-family:"Noto Sans JP",sans-serif}
.abs{position:absolute}
.btn{position:absolute;display:flex;align-items:center;justify-content:center;background:var(--blue-soft);color:var(--ink);border-radius:40px;font-size:17px;font-weight:500;height:52px}
.sec-title{position:absolute;left:0;width:1200px;text-align:center;font-size:26px;font-weight:500;letter-spacing:2px}
.sec-title::after{content:"";display:block;width:70px;height:2px;background:var(--blue);margin:14px auto 0}
.photo{position:absolute}
/* header */
.logo{left:40px;top:40px;display:flex;align-items:center;gap:12px;font-size:30px;font-weight:500;color:var(--blue)}
.logo i{width:26px;height:26px;border-radius:50%;background:var(--blue);display:block}
.tel{left:700px;top:40px;font-size:34px;font-weight:500;display:flex;align-items:center;gap:10px}
.tel-sub{left:756px;top:86px;font-size:14px;color:var(--muted)}
.mail-btn{left:990px;top:28px;width:190px;height:100px;border-radius:50px;background:var(--blue-soft);display:flex;flex-direction:column;align-items:center;justify-content:center;gap:6px;font-size:16px;color:var(--white)}
/* hero */
.hero{left:0;top:150px;width:1200px;height:540px;background:linear-gradient(120deg,#dfe9f0,#c9d7e2 45%,#eef2f4)}
.hero-text{left:190px;top:370px;color:var(--white);white-space:nowrap}
.hero-text p{font-size:44px;font-weight:500;letter-spacing:2px}
.hero-text h1{font-size:36px;font-weight:500;margin-top:6px;letter-spacing:1px}
.hero-text h1 em{font-style:normal;font-size:52px;font-weight:700}
/* nav */
.nav{left:100px;top:722px;width:1000px;display:flex;justify-content:space-between;font-size:17px}
/* features */
.globe{left:-60px;top:960px;width:620px;height:620px;border-radius:50%;background:radial-gradient(circle at 50% 40%,#d7ecf7,#6f9b6a 60%,#3f6b3c);overflow:hidden}
.feature{left:590px;width:560px}
.feature .num{font-size:64px;font-weight:300;color:var(--ink);line-height:1;float:left;margin-right:20px}
.feature h3{font-size:22px;font-weight:500;padding-top:26px}
.feature p{clear:both;font-size:14px;line-height:1.8;color:var(--muted);padding-left:60px;padding-top:10px}
/* services */
.svc-photo{left:0;top:1840px;width:1200px;height:430px;background:linear-gradient(90deg,#eceae6,#d8cfc4 40%,#f1f0ee 70%,#e3e6ea)}
.svc h3{font-size:20px;font-weight:500;text-align:center}
.svc p{font-size:13px;line-height:1.8;color:var(--muted);margin-top:16px}
/* usage */
.usage{left:0;top:2590px;width:1200px;height:355px;background:var(--blue-pale)}
.hex{left:230px;top:2720px}
/* news */
.news-box{left:150px;top:3140px;width:900px;height:380px;background:var(--blue-soft);border-radius:100px}
.news-row{left:370px;display:flex;gap:110px;font-size:14px;color:var(--ink)}
/* contact */
.contact{left:0;top:3630px;width:1200px;height:260px;background:var(--blue-pale)}
/* recruit */
.rec-photo{left:200px;top:4090px;width:800px;height:380px;border-radius:190px;background:linear-gradient(180deg,#cfe3ee,#9fbf88 60%,#6f9167)}
.circle{position:absolute;top:4540px;width:260px;height:260px;border-radius:50%;background:var(--blue-pale);display:flex;flex-direction:column;align-items:center;justify-content:center;padding:30px;text-align:center}
.circle h4{font-size:14px;font-weight:500}
.circle p{font-size:12px;color:var(--muted);line-height:1.7;margin-top:14px}
.foot{left:100px;top:5188px;width:1000px;display:flex;justify-content:space-between;font-size:15px}
</style>
</head>
<body>

<header>
  <div class="abs logo"><i></i>訪問介護そよぎ</div>
  <div class="abs tel">
    <svg width="36" height="36" viewBox="0 0 24 24" fill="none" stroke="#333a40" stroke-width="1.6"><path d="M5 3h4l2 5-3 2a12 12 0 0 0 6 6l2-3 5 2v4a2 2 0 0 1-2 2A17 17 0 0 1 3 5a2 2 0 0 1 2-2z"/></svg>
    012-345-6789
  </div>
  <div class="abs tel-sub">受付 9:00〜18:00</div>
  <div class="abs mail-btn">
    <svg width="40" height="28" viewBox="0 0 40 28" fill="none" stroke="#fff" stroke-width="2"><rect x="1" y="1" width="38" height="26"/><path d="M1 1l19 15L39 1"/></svg>
    メールで問い合わせ
  </div>
</header>

<section>
  <div class="abs hero" role="img" aria-label="高齢者の手に寄り添う介護者の手の写真"></div>
  <div class="abs hero-text">
    <p>24時間365日</p>
    <h1>住み慣れたご自宅で“<em>自分らしい</em>”介護サービスを</h1>
  </div>
</section>

<nav class="abs nav">
  <span>特徴</span><span>ご利用について</span><span>提供サービス</span><span>事業所一覧</span><span>採用情報</span><span>運営会社</span>
</nav>

<section>
  <h2 class="sec-title" style="top:870px">訪問介護そよぎの特徴</h2>
  <div class="photo globe" role="img" aria-label="苔の上に置かれたガラスの地球儀の写真"></div>
  <div class="abs feature" style="top:1040px">
    <span class="num">1</span><h3>24時間365日対応</h3>
    <p>夜間や休日でも安心してご利用いただけるよう、<br>いつでも必要な介護サービスを提供しています。<br>急なご相談にも経験豊富なスタッフが対応します。</p>
  </div>
  <div class="abs feature" style="top:1215px">
    <span class="num">2</span><h3>1人ひとりに最適な個別支援</h3>
    <p>ご本人とご家族のお話を丁寧に伺い、<br>生活に合わせたケアプランを作成します。<br>その方らしい暮らしを大切にしています。</p>
  </div>
  <div class="abs feature" style="top:1390px">
    <span class="num">3</span><h3>高齢者から障がい者・児まで</h3>
    <p>年齢や障がいの有無にかかわらず、<br>幅広い方々の在宅生活を支えます。<br>地域の関係機関とも連携しています。</p>
  </div>
  <div class="btn" style="left:860px;top:1580px;width:230px">特徴を詳しく見る</div>
</section>

<section>
  <h2 class="sec-title" style="top:1740px">提供サービス</h2>
  <div class="photo svc-photo" role="img" aria-label="食事介助をする介護スタッフと手のひらに乗せたミニチュアの写真"></div>
  <div class="abs svc" style="left:60px;top:2290px;width:470px">
    <h3>訪問介護</h3>
    <p>専門資格を持つヘルパーがご自宅を訪問し、身体介護や生活援助を行います。<br>日常の困りごとにも丁寧に寄り添います。</p>
  </div>
  <div class="abs svc" style="left:670px;top:2290px;width:470px">
    <h3>居宅介護支援</h3>
    <p>ケアマネジャーがご本人やご家族と相談しながら、介護保険の申請や<br>ケアプランの作成、サービス事業者との調整を行います。</p>
  </div>
  <div class="btn" style="left:365px;top:2400px;width:220px">詳しく見る</div>
  <div class="btn" style="left:960px;top:2400px;width:220px">詳しく見る</div>
</section>

<section>
  <div class="abs usage"></div>
  <h2 class="sec-title" style="top:2625px">ご利用について</h2>
  <svg class="abs hex" width="200" height="150" viewBox="0 0 200 150"><polygon points="45,5 155,5 198,75 155,145 45,145 2,75" fill="#fff"/><text x="100" y="84" text-anchor="middle" font-size="24" font-family="Noto Sans JP, sans-serif" fill="#333a40">手続き</text></svg>
  <div class="abs" style="left:520px;top:2745px;font-size:21px;font-weight:500">訪問介護のご利用には要介護認定が必要です</div>
  <div class="abs" style="left:520px;top:2795px;font-size:13px;line-height:1.8;color:var(--muted)">まずはお住まいの市町村窓口へ要介護認定の申請をおこなってください。<br>認定後はケアプランを作成し、サービス開始となります。</div>
  <div class="btn" style="left:880px;top:2860px;width:300px;background:var(--white)">利用の流れを詳しく見る</div>
</section>

<section>
  <h2 class="sec-title" style="top:3045px">お知らせ</h2>
  <div class="abs news-box"></div>
  <div class="abs news-row" style="top:3235px"><span>0000.00</span><span>新事業所オープン</span></div>
  <div class="abs news-row" style="top:3300px"><span>0000.00</span><span>サービス提供地域を拡大しました</span></div>
  <div class="abs news-row" style="top:3365px"><span>0000.00</span><span>登録ヘルパー募集します</span></div>
  <div class="btn" style="left:800px;top:3420px;width:200px;background:var(--white)">一覧を見る</div>
</section>

<section>
  <div class="abs contact"></div>
  <div class="abs" style="left:0;width:1200px;top:3675px;text-align:center;font-size:18px;font-weight:500">無料相談受付中！お気軽にお問い合わせください</div>
  <div class="abs tel" style="left:300px;top:3745px">
    <svg width="40" height="40" viewBox="0 0 24 24" fill="none" stroke="#333a40" stroke-width="1.6"><path d="M5 3h4l2 5-3 2a12 12 0 0 0 6 6l2-3 5 2v4a2 2 0 0 1-2 2A17 17 0 0 1 3 5a2 2 0 0 1 2-2z"/></svg>
    012-345-6789
  </div>
  <div class="abs tel-sub" style="left:356px;top:3795px">受付 9:00〜18:00</div>
  <div class="abs" style="left:660px;top:3730px;width:230px;height:110px;border-radius:55px;background:var(--white);display:flex;flex-direction:column;align-items:center;justify-content:center;gap:8px;font-size:18px">
    メールで問い合わせ
    <svg width="40" height="28" viewBox="0 0 40 28" fill="none" stroke="#333a40" stroke-width="2"><rect x="1" y="1" width="38" height="26"/><path d="M1 1l19 15L39 1"/></svg>
  </div>
</section>

<section>
  <div class="abs" style="left:0;width:1200px;top:3965px;text-align:center;font-size:14px;color:var(--muted)">“介護を通じて笑顔を届けたい” 地域の皆様の声にお応えするために</div>
  <h2 class="sec-title" style="top:4000px;font-size:30px">スタッフ積極採用中</h2>
  <div class="photo rec-photo" role="img" aria-label="車椅子の高齢者に寄り添う介護スタッフの屋外写真"></div>
  <div class="circle" style="left:200px"><h4>車両費・ガソリン代全額会社負担</h4><p>ガソリン代・車両代・<br>メンテナンス費・駐車場代<br>すべて会社が負担します。</p></div>
  <div class="circle" style="left:470px"><h4>週1日1時間〜短時間勤務も可能</h4><p>週1日からOK。<br>ライフスタイルに合わせて<br>無理なく働けます。</p></div>
  <div class="circle" style="left:740px"><h4>賞与・退職金制度あり</h4><p>資格取得支援や<br>キャリアアップ制度も充実。<br>長く働ける環境です。</p></div>
  <div class="btn" style="left:500px;top:4900px;width:200px">採用情報 &gt;</div>
</section>

<footer class="abs foot">
  <span>特徴</span><span>ご利用について</span><span>提供サービス</span><span>事業所一覧</span><span>採用情報</span><span>運営会社</span>
</footer>

</body>
</html>
```